Flyer for Aluminium recycling business

We are a startup aluminium recycling business. We don’t have a logo yet. I’ve attached a flyer created by one of our sales people but it’s a bit average and we need something a bit more modern and slick. You have creative license to completely change everything - as long as the information being communicated is the same.

Target Market(s)

Hospitality, Hotels, Apartment blocks, malls etcs

Industry/Entity Type

Aluminium recycling

Requirements
Must have
• the wording
Nice to have
• you have free license on design aspect

```html
<!DOCTYPE html>
<html lang="en">
<head>
<meta charset="utf-8">
<title>Aluminium Recycling Flyer</title>
<link rel="stylesheet" href="https://fonts.googleapis.com/css2?family=Outfit:wght@500;600;700&family=Quicksand:wght@500;600;700&display=swap">
<style>
  :root{
    --page:#d3d3d3;
    --cyan:#00cdd1;
    --navy:#0b3358;
    --ink:#0e1b26;
    --deep:#0a2238;
    --hero-a:#23394b;
    --hero-b:#0d1f2d;
    --white:#ffffff;
  }
  *{box-sizing:border-box;margin:0;padding:0}
  html,body{width:890px;height:1200px;overflow:hidden;background:var(--page)}
  .flyer{position:absolute;left:114px;top:104px;width:662px;height:992px;background:var(--white);overflow:hidden;font-family:"Quicksand",sans-serif;color:var(--ink)}
  .hero{position:absolute;left:0;top:0;width:662px;height:430px;background:radial-gradient(ellipse at 30% 30%,#2c4558 0%,transparent 60%),linear-gradient(160deg,var(--hero-a),var(--hero-b))}
  .headline{position:absolute;left:41px;top:56px;font-family:"Outfit",sans-serif;font-weight:700;font-size:40px;line-height:45px;letter-spacing:-0.3px;color:var(--white)}
  .headline .accent{color:var(--cyan)}
  .rule{position:absolute;left:43px;top:251px;width:116px;height:3px;background:var(--cyan)}
  .intro{position:absolute;left:42px;top:268px;width:260px;font-size:18px;font-weight:600;line-height:22px;color:var(--white)}
  .art{position:absolute;left:0;top:0}
  .simple-title{position:absolute;left:40px;top:455px;font-family:"Outfit",sans-serif;font-weight:700;font-size:36px;color:var(--navy);letter-spacing:-0.3px}
  .step-text{position:absolute;font-size:10px;font-weight:600;line-height:15px;color:var(--ink);text-align:justify}
  .step-1{left:34px;top:524px;width:108px}
  .step-2{left:34px;top:621px;width:108px}
  .step-3{left:348px;top:692px;width:100px;text-align:left}
  .step-4{left:497px;top:638px;width:120px}
  .step-5{left:499px;top:506px;width:128px}
  .examples-head{position:absolute;left:0;top:749px;width:662px;height:39px;background:var(--navy);color:var(--white);font-family:"Outfit",sans-serif;font-weight:600;font-size:24px;line-height:39px;text-align:center;letter-spacing:-0.2px}
  .examples{position:absolute;left:0;top:788px;width:662px;height:121px;background:var(--cyan)}
  .examples ul{position:absolute;list-style:none;top:12px}
  .examples .col-a{left:52px}
  .examples .col-b{left:357px}
  .examples li{position:relative;padding-left:23px;font-size:16.5px;font-weight:600;line-height:17.5px;color:var(--white);margin-bottom:9px}
  .examples li::before{content:"";position:absolute;left:0;top:2px;width:14px;height:14px;background:var(--navy);clip-path:polygon(50% 0,100% 25%,100% 75%,50% 100%,0 75%,0 25%)}
  .examples li::after{content:"";position:absolute;left:4.5px;top:6.5px;width:5px;height:5px;border-radius:50%;background:var(--white)}
  .footer-phone{position:absolute;left:0;top:909px;width:336px;height:81px;background:var(--deep)}
  .footer-mail{position:absolute;left:336px;top:909px;width:326px;height:81px;background:var(--navy);border-left:1.5px solid var(--cyan)}
  .footer-line{position:absolute;left:0;top:990px;width:662px;height:2px;background:var(--cyan)}
  .phone-number{position:absolute;left:71px;top:15px;font-family:"Outfit",sans-serif;font-weight:700;font-size:37px;color:var(--white);letter-spacing:-0.5px}
  .phone-icon{position:absolute;left:22px;top:22px}
  .mail-icon{position:absolute;left:29px;top:23px;width:34px;height:34px;border-radius:4px;background:var(--cyan)}
  .mail-label{position:absolute;left:73px;top:20px;width:212px;font-size:14px;font-weight:700;color:var(--cyan);display:flex;align-items:center;gap:4px}
  .mail-label::after{content:"";flex:1;border-top:1px dotted var(--cyan)}
  .mail-address{position:absolute;left:72px;top:40px;font-size:15px;font-weight:600;color:var(--white)}
</style>
</head>
<body>
<div class="flyer">
  <div class="hero" role="img" aria-label="Blurred dark blue backdrop of a recycling yard"></div>

  <h1 class="headline">PLAYING THE<br><span class="accent">FAIR ALUMINIUM<br>RECYCLING GAME</span><br>FOR GOOD</h1>
  <div class="rule"></div>
  <p class="intro">Our partnership with you is based on common sense, mutual gain and a better tomorrow</p>

  <svg class="art" width="662" height="760" viewBox="0 0 662 760">
    <defs>
      <linearGradient id="scrap" x1="0" y1="0" x2="1" y2="1">
        <stop offset="0" stop-color="#5a6168"/><stop offset="0.5" stop-color="#2a2f35"/><stop offset="1" stop-color="#70777e"/>
      </linearGradient>
      <linearGradient id="cans" x1="0" y1="0" x2="1" y2="1">
        <stop offset="0" stop-color="#b8c4c8"/><stop offset="0.5" stop-color="#7f8d92"/><stop offset="1" stop-color="#4e5a5f"/>
      </linearGradient>
      <linearGradient id="cans2" x1="0" y1="0" x2="1" y2="1">
        <stop offset="0" stop-color="#6b6256"/><stop offset="0.5" stop-color="#aeb3b2"/><stop offset="1" stop-color="#5b6266"/>
      </linearGradient>
    </defs>
    <!-- hexagon frames -->
    <polygon points="526,47 637,110 637,234 526,297 415,234 415,110" fill="none" stroke="var(--cyan)" stroke-width="3"/>
    <polygon role="img" aria-label="Photo of shredded aluminium scrap" points="526,57 629,115 629,229 526,287 423,229 423,115" fill="url(#scrap)" stroke="var(--white)" stroke-width="2"/>
    <polygon points="414,241 524,304 524,431 414,494 303,431 303,304" fill="var(--white)" stroke="var(--cyan)" stroke-width="3"/>
    <polygon role="img" aria-label="Photo of crushed aluminium cans" points="414,251 516,309 516,426 414,484 311,426 311,309" fill="url(#cans)"/>
    <polygon points="638,241 748,304 748,431 638,494 528,431 528,304" fill="var(--white)" stroke="var(--cyan)" stroke-width="3"/>
    <polygon role="img" aria-label="Photo of used beverage cans" points="638,251 740,309 740,426 638,484 536,426 536,309" fill="url(#cans2)"/>
    <polygon points="662,227 662,248 640,240" fill="var(--cyan)"/>
    <polygon points="526,437 545,448 545,470 526,481 507,470 507,448" fill="var(--cyan)"/>

    <!-- connectors -->
    <g fill="none" stroke="var(--navy)" stroke-width="1">
      <path d="M169 552 V572 Q169 582 179 582 H252"/>
      <path d="M252 605 H179 Q169 605 169 615 V639"/>
      <path d="M321 664 V687"/>
      <path d="M392 605 H459 Q469 605 469 615 V639"/>
      <path d="M392 582 H461 Q471 582 471 572 V552"/>
    </g>

    <!-- central badge -->
    <circle cx="321" cy="594" r="70" fill="var(--cyan)"/>
    <circle cx="321" cy="594" r="59" fill="var(--navy)" stroke="var(--white)" stroke-width="2"/>
    <g fill="none" stroke="var(--cyan)" stroke-width="7" stroke-linecap="round">
      <path d="M303 580 A22 22 0 0 1 335 574"/>
      <path d="M342 592 A22 22 0 0 1 327 619"/>
      <path d="M310 617 A22 22 0 0 1 300 592"/>
    </g>
    <g fill="var(--cyan)">
      <polygon points="333,564 346,578 329,582"/>
      <polygon points="334,613 322,629 316,613"/>
      <polygon points="292,597 296,577 308,591"/>
    </g>

    <!-- step markers -->
    <g fill="var(--cyan)" stroke="var(--white)" stroke-width="1.5">
      <polygon points="169,514 186,524 186,543 169,553 152,543 152,524"/>
      <polygon points="169,639 186,649 186,668 169,678 152,668 152,649"/>
      <polygon points="322,687 339,697 339,716 322,726 305,716 305,697"/>
      <polygon points="469,639 486,649 486,668 469,678 452,668 452,649"/>
      <polygon points="471,514 488,524 488,543 471,553 454,543 454,524"/>
    </g>
    <g fill="var(--white)" font-family="Outfit, sans-serif" font-weight="700" font-size="26" text-anchor="middle">
      <text x="169" y="543">1</text>
      <text x="169" y="668">2</text>
      <text x="322" y="716">3</text>
      <text x="469" y="668">4</text>
      <text x="471" y="543">5</text>
    </g>
  </svg>

  <h2 class="simple-title">IT'S SIMPLE</h2>

  <p class="step-text step-1">We bring you a free bin</p>
  <p class="step-text step-2">You throw all and any aluminium waste into the bin - no need to super-clean it. Try to compact/squash the aluminium as much as possible</p>
  <p class="step-text step-3">We collect the bin at no charge</p>
  <p class="step-text step-4">We turn the aluminium waste into a desirable resource</p>
  <p class="step-text step-5">We pay you for however much of that resource your waste has generated - and give you a report on that, so you can see how good you are</p>

  <h2 class="examples-head">EXAMPLES OF WHAT WE CAN TAKE</h2>
  <div class="examples">
    <ul class="col-a">
      <li>Used beverage cans - any</li>
      <li>Tinfoil-scrunched, crusty, burned<br>or dirty</li>
      <li>Disposable BBQ roasting trays</li>
    </ul>
    <ul class="col-b">
      <li>Aluminium takeaway containers</li>
      <li>Wine bottle screw tops (and<br>collars - if you can get them off)</li>
      <li>Tear-off can lids</li>
    </ul>
  </div>

  <div class="footer-phone">
    <svg class="phone-icon" width="38" height="38" viewBox="0 0 38 38" aria-hidden="true">
      <path d="M8 4 L14 4 L16 12 L12 15 Q15 23 23 26 L26 22 L34 24 L34 30 Q34 34 30 34 Q6 32 4 8 Q4 4 8 4Z" fill="var(--cyan)"/>
      <path d="M21 10 A8 8 0 0 1 28 17 M21 4 A14 14 0 0 1 34 17" fill="none" stroke="var(--cyan)" stroke-width="2.5" stroke-linecap="round"/>
    </svg>
    <div class="phone-number">021 555 0147</div>
  </div>
  <div class="footer-mail">
    <div class="mail-icon">
      <svg width="34" height="34" viewBox="0 0 34 34" aria-hidden="true">
        <rect x="8" y="11" width="18" height="13" fill="none" stroke="var(--white)" stroke-width="1.8"/>
        <path d="M8 11 L17 18 L26 11 M8 24 L14 17 M26 24 L20 17" fill="none" stroke="var(--white)" stroke-width="1.8"/>
      </svg>
    </div>
    <div class="mail-label">EMAIL US</div>
    <div class="mail-address">hello@brightcanreclaim.co.nz</div>
  </div>
  <div class="footer-line"></div>
</div>
</body>
</html>
```